Startup Drone Platform Company business card

We are needing a business card design for our employees. We are a startup drone platform. We are looking for a business card that has our logo on one side, with the employee/company details on the opposite side. We are looking for something that is very eye catching, modern, and bold.

Target Market(s)

This will target both drone pilots and drone businesses, along with all the industries that could utilize drone services (aerial video, aerial photos, inspections, 3d mapping, etc).

Industry/Entity Type

Business

```html
<!DOCTYPE html>
<html lang="en">
<head>
<meta charset="utf-8">
<title>Hoverline – Business Card</title>
<link rel="stylesheet" href="https://fonts.googleapis.com/css2?family=Montserrat:wght@500&family=Open+Sans:wght@300;400;600&display=swap">
<style>
  :root {
    --navy: #13152f;
    --teal: #2bb7c4;
    --white: #ffffff;
    --muted: #d6d8e4;
    --backdrop: #e9e6e1;
    --card-w: 560px;
    --card-h: 320px;
  }
  * { box-sizing: border-box; margin: 0; padding: 0; }
  html, body {
    width: 1200px;
    height: 783px;
    overflow: hidden;
    background: var(--backdrop);
  }
  .canvas {
    position: relative;
    width: 1200px;
    height: 783px;
  }
  .card {
    position: absolute;
    width: var(--card-w);
    height: var(--card-h);
    background: var(--navy);
    color: var(--white);
    box-shadow: 0 6px 18px rgba(0, 0, 0, 0.18);
  }

  /* Front: logo side, rounded right end */
  .card--front {
    left: 50px;
    top: 80px;
    border-radius: 0 160px 160px 0;
    display: flex;
    align-items: center;
    justify-content: center;
  }
  .brand-line {
    display: flex;
    align-items: center;
    gap: 22px;
    padding-left: 30px;
  }
  .brand-dot {
    width: 34px;
    height: 34px;
    border-radius: 50%;
    border: 3px solid var(--teal);
  }
  .brand-name {
    font-family: "Montserrat", sans-serif;
    font-weight: 500;
    font-size: 40px;
    letter-spacing: 0.45em;
    color: var(--white);
  }

  /* Back: details side, rounded left end */
  .card--back {
    left: 590px;
    top: 383px;
    border-radius: 160px 0 0 160px;
    display: flex;
  }
  .back-brand {
    width: 250px;
    display: flex;
    flex-direction: column;
    align-items: center;
    justify-content: center;
    padding-left: 20px;
  }
  .back-brand .brand-dot {
    width: 120px;
    height: 120px;
    border-width: 4px;
    border-color: var(--white);
    margin-bottom: 26px;
  }
  .back-brand .brand-name {
    font-size: 26px;
    letter-spacing: 0.4em;
    text-align: center;
    line-height: 1.35;
    padding-left: 0.4em;
  }
  .details {
    flex: 1;
    font-family: "Open Sans", sans-serif;
    padding: 40px 34px 0 16px;
    text-align: center;
  }
  .person-name {
    font-weight: 600;
    font-size: 30px;
    color: var(--teal);
    line-height: 1.1;
  }
  .person-role {
    font-weight: 300;
    font-size: 15px;
    color: var(--muted);
    margin-bottom: 34px;
  }
  .contact {
    list-style: none;
    text-align: left;
    font-size: 15px;
    line-height: 1.8;
    margin-bottom: 26px;
  }
  .contact-label {
    color: var(--teal);
    margin-right: 8px;
  }
  .address {
    font-style: normal;
    font-size: 15px;
    line-height: 1.35;
    margin-bottom: 24px;
  }
  .website {
    font-size: 15px;
    color: var(--teal);
  }
</style>
</head>
<body>
  <main class="canvas">
    <section class="card card--front" aria-label="Card front">
      <div class="brand-line">
        <span class="brand-dot"></span>
        <span class="brand-name">HOVERLINE</span>
      </div>
    </section>

    <section class="card card--back" aria-label="Card back">
      <div class="back-brand">
        <span class="brand-dot"></span>
        <span class="brand-name">HOVER<br>LINE</span>
      </div>
      <div class="details">
        <h1 class="person-name">Daniel Moreau</h1>
        <p class="person-role">Technician</p>
        <ul class="contact">
          <li><span class="contact-label">t:</span>019876543</li>
          <li><span class="contact-label">e:</span>dmoreau@hoverline.com</li>
        </ul>
        <address class="address">1420 Harbor Lane<br>Westfield BA, 24680</address>
        <p class="website">www.hoverline.com</p>
      </div>
    </section>
  </main>
</body>
</html>
```